BrivoMatex. Lantern for the Steady Growth. Business card

Professional business card for BrivoMatex (Lantern for the Steady Growth)
My rationale: Strategy-> Execution-> Results-> Value that lead to the BrivoMatex name: We put the Lantern for the Steady Growth.
We deliver value to our customers helping them at defining a good strategy (cyan arrow). 90% of well formulated strategies fail due to poor execution so we also consider strategical execution very important (green arrow). Due to the execution we obtain the results (blue arrow). Finally, the results provide feedback to redefine strategy, and the new strategy has to be executed and new results obtained providing new feedback and on and on. It's like a wheel that finally, must create corporate value: value for shareholders, staholders, employees, providers...-

Target Market(s)

CEOs and steering comitees , invewrnent funds

Industry/Entity Type

Business Consultant

Contact Information for Business Card

Tommaso Ferlini
CEO & Founder
tommaso.ferlini@brivomatex.example
Mobile: +34 611.205.938
www.brivomatex.example

Colors

Designer to choose colors to be used in the design.

Requirements
Nice to have
• Nice to hace the words: Strategy, execution, results
• Nice to vave the claim: Lantern for the Steady Growth
• The three colors should be shown:
• cyan for STRATEGY
• green for EXECUTION
• blue for RESULTS
Should not have
• Complete black background

```html
<!DOCTYPE html>
<html lang="en">
<head>
<meta charset="utf-8">
<title>BrivoMatex — Business Card</title>
<link rel="stylesheet" href="https://fonts.googleapis.com/css2?family=Carlito:wght@400;700&family=Open+Sans:wght@300;400&display=swap">
<style>
  :root {
    --backdrop: #ececec;
    --execution-green: #9acd35;
    --strategy-cyan: #00aeef;
    --ink-white: #ffffff;
    --tagline-tint: #d8eeb4;
    --title-tint: #c4ecfc;
  }
  * { margin: 0; padding: 0; box-sizing: border-box; }
  html, body {
    width: 1200px;
    height: 851px;
    overflow: hidden;
    background: var(--backdrop);
  }
  .sheet {
    position: relative;
    width: 1200px;
    height: 851px;
  }
  .card {
    position: absolute;
    width: 405px;
    height: 231px;
    color: var(--ink-white);
  }
  .card--front {
    left: 168px;
    top: 310px;
    background: var(--execution-green);
  }
  .card--back {
    left: 628px;
    top: 309px;
    background: var(--strategy-cyan);
    font-family: "Carlito", "Calibri", sans-serif;
    text-align: right;
  }
  .brand-name {
    position: absolute;
    left: 0;
    right: 0;
    top: 136px;
    text-align: center;
    font-family: "Carlito", "Calibri", sans-serif;
    font-weight: 700;
    font-size: 44px;
    line-height: 1;
    letter-spacing: -0.5px;
    color: var(--ink-white);
  }
  .tagline {
    position: absolute;
    left: 0;
    right: 0;
    top: 203px;
    text-align: center;
    font-family: "Open Sans", sans-serif;
    font-weight: 300;
    font-size: 8.5px;
    letter-spacing: 1.8px;
    color: var(--tagline-tint);
  }
  .tagline .sep { margin: 0 5px; }
  .person {
    position: absolute;
    right: 19px;
    top: 16px;
  }
  .person__name {
    font-weight: 700;
    font-size: 14.5px;
    line-height: 1.05;
  }
  .person__role {
    font-weight: 400;
    font-size: 12px;
    line-height: 1.15;
    color: var(--title-tint);
  }
  .contact {
    position: absolute;
    right: 19px;
    top: 162px;
    list-style: none;
    font-size: 14px;
    line-height: 18.5px;
  }
</style>
</head>
<body>
  <main class="sheet">
    <section class="card card--front" aria-label="Card front">
      <div class="brand-name">BrivoMatex</div>
      <p class="tagline">STRATEGY<span class="sep">.</span>EXECUTION<span class="sep">.</span>RESULTS</p>
    </section>

    <section class="card card--back" aria-label="Card back">
      <div class="person">
        <p class="person__name">Tommaso FERLINI</p>
        <p class="person__role">CEO &amp; Founder</p>
      </div>
      <ul class="contact">
        <li>+34 611 205 938</li>
        <li>tommaso.ferlini@brivomatex.example</li>
        <li>www.brivomatex.example</li>
      </ul>
    </section>
  </main>
</body>
</html>
```